Blog Webpage - Paw Harbour Ltd

Hello!!!!

Looking to incorporate a blog page on our current website www.pawharbour.co.uk. (Veterinary Recruitment Agency) The one we have is not very user friendly and is very limited in terms of what content can be added. Our current website is mainly word press, but if at all possible we would be looking for a HTML/Similar coded blog page to be added like our jobs page https://pawharbourjobs.brindlehire.com/ that seems to be picked up more by search engines.

Key Points:
1. Simple/user friendly, easy to update blog information I.e. updates from us, industry news, help/advice etc.
2. Updates to be added on a daily/weekly basis
3. Functionality’s like you have in a word document or similar – Front/Size/Colour etc.
4. Ease of upload/add written documents/images/graphics/vids etc.
5. Ability to easily amend/move content
6. Merge in with our current site/existing brand.
7. Ability to share on social media and mailers
8. SEO options
9. Add events
10. Manage customer comments
11. Ability for others to comment and for us to manage these
12. Possibly for these comments to be emailed to us, so we can pick them up ASAP?
13. Security and User login
14. Possibly page analytics
15. Like our FB, Twitter, Link, Google Plus pages etc
16. Ability to add competitions/surveys to be filled in

Many thanks for viewing this and hope someone can help!

Thanks Colin

Target Market(s)

Blog Webpage - Veterinary Recruitment Agency

Industry/Entity Type

Recruitment

Coding

Coded - Design and coding required

Font styles to use
Sans Serif

Colors
0555a3
9bcb3c

Requirements
Must have
• HTML/Similar
Nice to have
• As per brief

```html
<!DOCTYPE html>
<html lang="en">
<head>
<meta charset="utf-8">
<title>Paw Harbour Chatter – Blog</title>
<link href="https://fonts.googleapis.com/css2?family=Mulish:wght@400;600;700&family=Open+Sans:wght@400;600;700&display=swap" rel="stylesheet">
<style>
:root{
  --blue:#0555a3;
  --blue-dark:#0b3f7a;
  --navy:#0a3a6b;
  --green:#9bcb3c;
  --text:#1d3d6b;
  --grey:#6f6f6f;
  --line:#d9d9d9;
  --nav-bg:#ececec;
  --page:#ffffff;
  --dot-1:#3b5998;
  --dot-2:#d34836;
  --dot-3:#2aa3e0;
  --dot-4:#0d77b7;
}
*{box-sizing:border-box;margin:0;padding:0}
html,body{width:1200px;height:3279px;overflow:hidden}
body{position:relative;background:var(--page);font-family:"Open Sans",Arial,sans-serif;color:var(--grey)}
a{color:inherit;text-decoration:none}
.abs{position:absolute}

/* header */
.brand{left:125px;top:24px;display:flex;align-items:center;gap:12px}
.brand-dot{width:58px;height:58px;border-radius:50%;background:var(--blue)}
.brand-name{font-family:"Mulish",sans-serif;font-weight:700;font-size:32px;color:var(--blue)}
.btn-register,.btn-timesheet{top:39px;height:40px;display:flex;align-items:center;justify-content:center;font-size:16px;font-family:"Mulish",sans-serif}
.btn-register{left:428px;width:169px;border:2px solid var(--blue);color:var(--blue)}
.btn-timesheet{left:608px;width:179px;border:2px solid var(--green);color:var(--green)}
.contact{left:890px;top:30px;font-size:19px;color:var(--blue);line-height:31px;font-family:"Mulish",sans-serif}
.contact div{display:flex;align-items:center;gap:9px}
.contact .mail{font-size:17px}

.main-nav{left:0;top:114px;width:1200px;height:56px;background:var(--nav-bg)}
.main-nav ul{position:absolute;left:135px;top:0;display:flex;list-style:none;height:56px}
.main-nav li{display:flex;align-items:center;justify-content:center;border-right:1px solid #cfcfcf;font-size:16px;color:#555;font-family:"Mulish",sans-serif}
.main-nav li:first-child{border-left:1px solid #cfcfcf}
.main-nav li.active{background:var(--blue);color:#fff}

/* hero */
.hero{left:0;top:170px;width:1200px;height:390px;background:linear-gradient(100deg,#4f8ec6 0%,#a9c8de 30%,#d9dfe4 50%,#8a6d56 66%,#cfd9e4 85%,#3f78b2 100%)}
.hero-title{left:116px;top:310px;width:393px;height:75px;background:var(--green);color:#fff;font-family:"Mulish",sans-serif;font-weight:600;font-size:35px;display:flex;align-items:center;padding-left:26px}
.hero-caption{left:0;top:503px;width:1200px;height:57px;background:rgba(20,40,70,.55);color:#fff;font-size:20px;display:flex;align-items:center;padding-left:124px}
.hero-arrows{right:120px;top:518px;display:flex;gap:20px}

/* posts */
.post{left:114px;width:664px;height:252px;border:1px solid var(--line);background:#fff;box-shadow:0 1px 3px rgba(0,0,0,.06)}
.post-image{position:absolute;left:17px;top:17px;width:262px;height:208px}
.post-body{position:absolute;left:301px;top:26px;right:20px}
.post-title{font-family:"Mulish",sans-serif;font-weight:700;font-size:18px;color:var(--text);margin-bottom:12px}
.post-excerpt{font-size:13px;line-height:22px;color:#666;height:66px;overflow:hidden}
.read-more{display:inline-flex;align-items:center;justify-content:center;width:109px;height:33px;border:2px solid var(--green);color:var(--green);font-size:11px;font-weight:600;margin-top:18px}
.post-meta{position:absolute;left:301px;bottom:22px;display:flex;align-items:center;gap:6px;font-size:12px;color:#777}
.post-meta .date{margin:0 10px 0 4px}
.share{width:26px;height:26px;border-radius:50%}
.share.s1{background:var(--dot-1)}.share.s2{background:var(--dot-2)}.share.s3{background:var(--dot-3)}.share.s4{background:var(--dot-4)}

.pager{left:368px;top:2791px;display:flex;gap:8px}
.pager span{width:32px;height:32px;border-radius:50%;border:1px solid #ccc;display:flex;align-items:center;justify-content:center;font-size:13px;color:#666}
.pager .current{background:var(--green);border-color:var(--green);color:#fff}

/* sidebar */
.widget{left:815px;width:272px;border:1px solid var(--line);background:#f4f4f4}
.widget-head{height:46px;display:flex;align-items:center;padding-left:18px;font-family:"Mulish",sans-serif;font-size:22px;color:#fff;background:var(--blue-dark)}
.widget-head.green{background:var(--green)}
.widget-head.plain{background:#fff;color:#555;font-size:17px;border-bottom:1px solid var(--line)}
.field{margin:0 18px 12px;height:36px;background:#fff;border:1px solid #ddd;font-size:11px;color:#777;display:flex;align-items:center;padding-left:12px}
.btn-green{margin:0 18px;height:38px;background:var(--green);color:#fff;font-size:13px;font-weight:700;display:flex;align-items:center;justify-content:center}
.comp-text{padding:18px 18px 14px;font-size:12px;line-height:19px;color:#777}
.cta{left:815px;width:272px;height:51px;display:flex;align-items:center;justify-content:center;gap:10px;color:#fff;font-family:"Mulish",sans-serif;font-size:22px;font-weight:600}
.cta.action{top:1167px;background:#2a6bb0}
.cta.cv{top:1229px;background:var(--navy)}
.comment{display:flex;gap:12px;padding:0 14px;margin-top:20px}
.avatar{flex:none;width:44px;height:44px;border-radius:50%;background:linear-gradient(135deg,#b9a08b,#e3d2c2)}
.comment h4,.news h4{font-size:12px;color:var(--blue);font-weight:600}
.comment p{font-size:10px;line-height:14px;color:#999}
.news{display:flex;gap:12px;padding:0 14px;margin-top:20px}
.news-thumb{flex:none;width:76px;height:76px;background:linear-gradient(135deg,#c99a6b,#e8dccb)}
.news p{font-size:10px;line-height:13px;color:#999}
.news b{font-size:9px;color:#333}
.follow{background:#fff;text-align:center}
.follow h3,.sub h3{font-family:"Mulish",sans-serif;font-weight:400;font-size:21px;color:#444}
.follow .circles{display:flex;gap:10px;justify-content:center;margin-top:12px}
.follow .share{width:36px;height:36px}
.sub{background:#fff;text-align:center}

/* footer */
.site-footer{left:0;top:2881px;width:1200px;height:324px;background:var(--blue)}
.foot-col{top:2940px;color:#fff}
.foot-col h3{font-family:"Mulish",sans-serif;font-weight:400;font-size:24px;margin-bottom:14px}
.foot-col li{list-style:none;font-size:14px;line-height:28.5px}
.news-input{left:761px;top:2990px;width:310px;height:42px;border:1px solid #fff;color:#fff;font-size:15px;display:flex;align-items:center;gap:10px;padding-left:14px}
.news-btn{left:761px;top:3045px;width:131px;height:40px;background:var(--green);color:#fff;font-size:16px;font-weight:600;display:flex;align-items:center;justify-content:center}
.footer-bar{left:0;top:3205px;width:1200px;height:74px;background:#0a4788;color:#9fb8d8;font-size:13px;display:flex;align-items:center;justify-content:center}
</style>
</head>
<body>

<header>
  <a class="brand abs" href="#"><span class="brand-dot"></span><span class="brand-name">Paw Harbour</span></a>
  <a class="btn-register abs" href="#">Register</a>
  <a class="btn-timesheet abs" href="#">Timesheet Portal</a>
  <div class="contact abs">
    <div><svg width="18" height="18" viewBox="0 0 24 24"><path d="M6.6 10.8a15 15 0 0 0 6.6 6.6l2.2-2.2a1 1 0 0 1 1-.25 11 11 0 0 0 3.6.6 1 1 0 0 1 1 1V20a1 1 0 0 1-1 1A17 17 0 0 1 3 4a1 1 0 0 1 1-1h3.5a1 1 0 0 1 1 1 11 11 0 0 0 .6 3.6 1 1 0 0 1-.25 1z" fill="none" stroke="#0555a3" stroke-width="1.8"/></svg>0333 000 4182</div>
    <div class="mail"><svg width="18" height="14" viewBox="0 0 18 14"><rect x="1" y="1" width="16" height="12" fill="none" stroke="#0555a3" stroke-width="1.6"/><path d="M1 1l8 6 8-6" fill="none" stroke="#0555a3" stroke-width="1.6"/></svg>info@pawharbour.co.uk</div>
  </div>
  <nav class="main-nav abs">
    <ul>
      <li style="width:73px">Home</li>
      <li style="width:120px">Job Seekers</li>
      <li style="width:77px">Clients</li>
      <li style="width:142px">Help &amp; Advice</li>
      <li style="width:170px">PH Loyalty Scheme</li>
      <li class="active" style="width:136px">News &amp; Blogs</li>
      <li style="width:100px">About Us</li>
      <li style="width:118px">Contact Us</li>
    </ul>
  </nav>
</header>

<section>
  <div class="hero abs" role="img" aria-label="Photo of a smiling husky dog with a vet holding a clipboard"></div>
  <h1 class="hero-title abs">Paw Harbour Chatter</h1>
  <div class="hero-caption abs">Maecenas aliquet velit vel turpis Mauris neque metus malesuada</div>
  <div class="hero-arrows abs">
    <svg width="12" height="20" viewBox="0 0 12 20"><path d="M10 2L2 10l8 8" fill="none" stroke="#fff" stroke-width="2"/></svg>
    <svg width="12" height="20" viewBox="0 0 12 20"><path d="M2 2l8 8-8 8" fill="none" stroke="#fff" stroke-width="2"/></svg>
  </div>
</section>

<main>
  <article class="post abs" style="top:612px">
    <div class="post-image" role="img" aria-label="Photo of a white kitten being examined by a vet" style="background:linear-gradient(135deg,#d8c8b8,#f1ece6)"></div>
    <div class="post-body"><h2 class="post-title">Waiter, there’s a FLY in my…</h2><p class="post-excerpt">The QUILLS REPORT I detest water. Frankly, I am troubled by it. It’s so, well, SPLASHY. Go-away, rain… Back-off, puddles… Think again, pond</p><a class="read-more" href="#">READ MORE</a></div>
    <div class="post-meta" aria-label="Share this post"><svg width="14" height="14" viewBox="0 0 14 14"><circle cx="7" cy="7" r="6" fill="none" stroke="#999"/><path d="M7 3v4h3" fill="none" stroke="#999"/></svg><span class="date">December 5, 2016</span><span class="share s1"></span><span class="share s2"></span><span class="share s3"></span><span class="share s4"></span></div>
  </article>

  <article class="post abs" style="top:882px">
    <div class="post-image" role="img" aria-label="Photo of a vet examining a ginger cat" style="background:linear-gradient(135deg,#6d9cc4,#d9c3a5)"></div>
    <div class="post-body"><h2 class="post-title">Maecenas aliquet velit vel turpis</h2><p class="post-excerpt">The QUILLS REPORT I detest water. Frankly, I am troubled by it. It’s so, well, SPLASHY. Go-away, rain… Back-off, puddles… Think again, pond</p><a class="read-more" href="#">READ MORE</a></div>
    <div class="post-meta" aria-label="Share this post"><svg width="14" height="14" viewBox="0 0 14 14"><circle cx="7" cy="7" r="6" fill="none" stroke="#999"/><path d="M7 3v4h3" fill="none" stroke="#999"/></svg><span class="date">December 5, 2016</span><span class="share s1"></span><span class="share s2"></span><span class="share s3"></span><span class="share s4"></span></div>
  </article>

  <article class="post abs" style="top:1152px">
    <div class="post-image" role="img" aria-label="Photo of a vet holding a small dog" style="background:linear-gradient(135deg,#c9b59e,#eeeae4)"></div>
    <div class="post-body"><h2 class="post-title">WARNING! YUCKY PHOTOS!</h2><p class="post-excerpt">The Myths and Realities of CAT BITES &amp; CAT SCRATCHES I try to keep at paws’ length distance from Tibs Pembury, my next-door neighbour; particular!</p><a class="read-more" href="#">READ MORE</a></div>
    <div class="post-meta" aria-label="Share this post"><svg width="14" height="14" viewBox="0 0 14 14"><circle cx="7" cy="7" r="6" fill="none" stroke="#999"/><path d="M7 3v4h3" fill="none" stroke="#999"/></svg><span class="date">December 5, 2016</span><span class="share s1"></span><span class="share s2"></span><span class="share s3"></span><span class="share s4"></span></div>
  </article>

  <article class="post abs" style="top:1422px">
    <div class="post-image" role="img" aria-label="Photo of a vet checking a dog's ear" style="background:linear-gradient(135deg,#b48a62,#e7dccd)"></div>
    <div class="post-body"><h2 class="post-title">Hare today(not) gone tomorrow</h2><p class="post-excerpt">Guest spot: Maren Oakley RVN If an injured or young hare has been brought in for treatment, would you know what to do? &amp;nb</p><a class="read-more" href="#">READ MORE</a></div>
    <div class="post-meta" aria-label="Share this post"><svg width="14" height="14" viewBox="0 0 14 14"><circle cx="7" cy="7" r="6" fill="none" stroke="#999"/><path d="M7 3v4h3" fill="none" stroke="#999"/></svg><span class="date">December 5, 2016</span><span class="share s1"></span><span class="share s2"></span><span class="share s3"></span><span class="share s4"></span></div>
  </article>

  <article class="post abs" style="top:1692px">
    <div class="post-image" role="img" aria-label="Photo of a vet with a puppy in a clinic" style="background:linear-gradient(135deg,#e4e8ec,#c7b092)"></div>
    <div class="post-body"><h2 class="post-title">Asking the boss for a pay raise</h2><p class="post-excerpt">A pay raise for Rusty? In the past I’ve often had to prompt my boss for more juicy beetles and ask them to</p><a class="read-more" href="#">READ MORE</a></div>
    <div class="post-meta" aria-label="Share this post"><svg width="14" height="14" viewBox="0 0 14 14"><circle cx="7" cy="7" r="6" fill="none" stroke="#999"/><path d="M7 3v4h3" fill="none" stroke="#999"/></svg><span class="date">December 5, 2016</span><span class="share s1"></span><span class="share s2"></span><span class="share s3"></span><span class="share s4"></span></div>
  </article>

  <article class="post abs" style="top:1962px">
    <div class="post-image" role="img" aria-label="Photo of a vet examining a tabby cat" style="background:linear-gradient(135deg,#8f8478,#e6e1da)"></div>
    <div class="post-body"><h2 class="post-title">The Quills Report BARBEQUE BITS!</h2><p class="post-excerpt">The Quills Report BARBEQUE BITS! In the past I’ve often had to prompt my boss for more juicy beetles and ask them to</p><a class="read-more" href="#">READ MORE</a></div>
    <div class="post-meta" aria-label="Share this post"><svg width="14" height="14" viewBox="0 0 14 14"><circle cx="7" cy="7" r="6" fill="none" stroke="#999"/><path d="M7 3v4h3" fill="none" stroke="#999"/></svg><span class="date">December 5, 2016</span><span class="share s1"></span><span class="share s2"></span><span class="share s3"></span><span class="share s4"></span></div>
  </article>

  <article class="post abs" style="top:2232px">
    <div class="post-image" role="img" aria-label="Photo of two vets with a dog on the table" style="background:linear-gradient(135deg,#c8a07a,#f0e7dc)"></div>
    <div class="post-body"><h2 class="post-title">Proin nulla arcu nonummy</h2><p class="post-excerpt">FOOOOOOD! Yum yum, and may I say, YUM! I’m on a patio table. I am sneakily hiding under a discarded napkin</p><a class="read-more" href="#">READ MORE</a></div>
    <div class="post-meta" aria-label="Share this post"><svg width="14" height="14" viewBox="0 0 14 14"><circle cx="7" cy="7" r="6" fill="none" stroke="#999"/><path d="M7 3v4h3" fill="none" stroke="#999"/></svg><span class="date">December 5, 2016</span><span class="share s1"></span><span class="share s2"></span><span class="share s3"></span><span class="share s4"></span></div>
  </article>

  <article class="post abs" style="top:2504px">
    <div class="post-image" role="img" aria-label="Photo of a vet team holding a puppy" style="background:linear-gradient(135deg,#b7a089,#ece6df)"></div>
    <div class="post-body"><h2 class="post-title">Proin nulla arcu nonummy</h2><p class="post-excerpt">FOOOOOOD! Yum yum, and may I say, YUM! I’m on a patio table. I am sneakily hiding under a discarded napkin</p><a class="read-more" href="#">READ MORE</a></div>
    <div class="post-meta" aria-label="Share this post"><svg width="14" height="14" viewBox="0 0 14 14"><circle cx="7" cy="7" r="6" fill="none" stroke="#999"/><path d="M7 3v4h3" fill="none" stroke="#999"/></svg><span class="date">December 5, 2016</span><span class="share s1"></span><span class="share s2"></span><span class="share s3"></span><span class="share s4"></span></div>
  </article>

  <nav class="pager abs"><span>‹</span><span class="current">1</span><span>2</span><span>3</span><span>›</span></nav>
</main>

<aside>
  <div class="widget abs" style="top:608px;height:297px">
    <div class="widget-head">Register with us</div>
    <div style="padding-top:12px"><div class="field">Name</div><div class="field">Email Address</div><div class="field">Job Sector</div><div class="field">Job Location</div><div class="btn-green">Subscribe</div></div>
  </div>

  <div class="widget abs" style="top:929px;height:212px">
    <div class="widget-head">Competition</div>
    <p class="comp-text">Aecloqu ad litora torquent per conubia nostra per inceptos hymenaeos Proin nulla arcu luctus dictum eget fermentum et lorem Nunc</p>
    <div class="btn-green">Click here</div>
  </div>

  <a class="cta action abs" href="#"><svg width="16" height="14" viewBox="0 0 16 14"><path d="M1 7h13M9 2l5 5-5 5" fill="none" stroke="#fff" stroke-width="2"/></svg>Click to Action</a>
  <a class="cta cv abs" href="#"><svg width="18" height="18" viewBox="0 0 18 18"><rect x="1" y="3" width="13" height="13" fill="none" stroke="#fff" stroke-width="1.8"/><path d="M7 11l1-3 7-7 2 2-7 7z" fill="#fff"/></svg>Submit Your CV</a>

  <div class="widget abs" style="top:1298px;height:396px;background:#fff">
    <div class="widget-head plain">Customer Comments</div>
    <div class="comment"><span class="avatar" role="img" aria-label="Customer portrait"></span><div><h4>Customer Name</h4><p>Conubia nostra per inceptos hymenaeos. Proin nulla arcu nonummy luctus dictum eget.</p></div></div>
    <div class="comment"><span class="avatar" role="img" aria-label="Customer portrait"></span><div><h4>Customer Name</h4><p>Conubia nostra per inceptos hymenaeos. Proin nulla arcu nonummy luctus dictum eget.</p></div></div>
    <div class="comment"><span class="avatar" role="img" aria-label="Customer portrait"></span><div><h4>Customer Name</h4><p>Conubia nostra per inceptos hymenaeos. Proin nulla arcu nonummy luctus dictum eget.</p></div></div>
    <div class="comment"><span class="avatar" role="img" aria-label="Customer portrait"></span><div><h4>Customer Name</h4><p>Conubia nostra per inceptos hymenaeos. Proin nulla arcu nonummy luctus dictum eget.</p></div></div>
  </div>

  <div class="widget abs" style="top:1718px;height:496px;background:#fff">
    <div class="widget-head green">Latest News</div>
    <div class="news"><span class="news-thumb" role="img" aria-label="Thumbnail of a cat"></span><div><h4>Waiter, there’s a FLY in my…</h4><p>Accum tempus eros curabitur vel mi sit amet magna.</p><b>READ MORE</b></div></div>
    <div class="news"><span class="news-thumb" role="img" aria-label="Thumbnail of a dog"></span><div><h4>WARNING! YUCKY PHOTOS</h4><p>Accum tempus eros curabitur vel mi sit amet magna.</p><b>READ MORE</b></div></div>
    <div class="news"><span class="news-thumb" role="img" aria-label="Thumbnail of a dog"></span><div><h4>Hare today(not) gone tomorrow</h4><p>Accum tempus eros curabitur vel mi sit amet magna.</p><b>READ MORE</b></div></div>
    <div class="news"><span class="news-thumb" role="img" aria-label="Thumbnail of a puppy"></span><div><h4>Asking the boss for a pay raise</h4><p>Accum tempus eros curabitur vel mi sit amet magna.</p><b>READ MORE</b></div></div>
  </div>

  <div class="widget follow abs" style="top:2228px;height:124px;padding-top:20px">
    <h3>Follow us on</h3>
    <div class="circles" aria-label="Follow us links"><span class="share s1"></span><span class="share s3"></span><span class="share s4"></span></div>
  </div>

  <div class="widget sub abs" style="top:2368px;height:183px;padding-top:22px">
    <h3>Subscribe to our<br>blog via email</h3>
    <div class="field" style="margin-top:16px;margin-bottom:10px;height:32px">Email address</div>
    <div class="btn-green" style="height:34px">Subscribe</div>
  </div>

  <div class="widget sub abs" style="top:2569px;height:164px;padding-top:22px">
    <h3>Subscribe via RSS</h3>
    <div class="field" style="margin-top:16px;margin-bottom:10px;height:32px">Email address</div>
    <div class="btn-green" style="height:34px">Subscribe</div>
  </div>
</aside>

<footer>
  <div class="site-footer abs"></div>
  <div class="foot-col abs" style="left:129px"><h3>Quick Links</h3><ul><li>Home</li><li>About us/Paw Harbour</li><li>Our service</li><li>Testimonials</li><li>Downloads</li></ul></div>
  <div class="foot-col abs" style="left:337px"><h3>Sublinks</h3><ul><li>Meet the team</li><li>Vision</li><li>Work for us</li><li>Register a vacancy</li><li>Enquiry</li></ul></div>
  <div class="foot-col abs" style="left:547px"><h3>Resources</h3><ul><li>Looking for staff</li><li>Contact</li><li>Offers/competition</li><li>News/blogs</li><li>Job seekers</li></ul></div>
  <div class="foot-col abs" style="left:761px"><h3>Join Our Newsletters</h3></div>
  <div class="news-input abs"><svg width="18" height="14" viewBox="0 0 18 14"><rect x="1" y="1" width="16" height="12" fill="none" stroke="#fff" stroke-width="1.6"/><path d="M1 1l8 6 8-6" fill="none" stroke="#fff" stroke-width="1.6"/></svg>Email address</div>
  <a class="news-btn abs" href="#">Subscribe</a>
  <div class="footer-bar abs">© 2017 Company Name. All right reserved. Term of Use</div>
</footer>

</body>
</html>
```